Corwyns Best 4 years in a row

I need a billboard that has all the attached logos and says:

Corwyn's Best Realtor 4 Years in a row!

1.75 Listing Fee

Tobias Wrenfield

555-214-7390

and somewhere very small at the bottom:

855-555-0142

2748 W Amberlow Rd, Bel Air, MD 20957

I put in the last winner just to give an idea of what I'm looking for, although I'd like to switch it up a little bit.

```html
<!DOCTYPE html>
<html lang="en">
<head>
<meta charset="utf-8">
<title>Corwyn's Best Realtor Billboard</title>
<link href="https://fonts.googleapis.com/css2?family=Poppins:wght@500;600;700;800&family=Oswald:wght@500;600&display=swap" rel="stylesheet">
<style>
  :root {
    --navy: #172f57;
    --orange: #ed7b2f;
    --white: #ffffff;
    --grey-stripe: #a3a3a3;
    --badge: #262626;
    --page: #e6e7ea;
  }
  * { margin: 0; padding: 0; box-sizing: border-box; }
  html, body { width: 1200px; height: 1200px; overflow: hidden; background: var(--page); }
  .billboard {
    position: absolute; left: 50px; top: 440px; width: 1100px; height: 320px;
    background: var(--white); overflow: hidden;
    box-shadow: 0 10px 30px rgba(0,0,0,.18);
  }
  .billboard-bg { position: absolute; inset: 0; }
  .agent-photo { position: absolute; left: 562px; top: 16px; width: 206px; height: 304px;
    border-radius: 90px 90px 0 0;
    background: linear-gradient(180deg, #b98b72 0%, #9c7664 26%, #2d3c5a 42%, #24324f 100%); }
  .award-badge { position: absolute; left: 704px; top: 38px; width: 92px; height: 92px;
    border-radius: 50%; background: var(--badge); }
  .accent-band { position: absolute; left: 0; top: 134px; height: 45px; width: 345px;
    background: var(--orange); clip-path: polygon(0 0, 318px 0, 345px 100%, 0 100%); }
  .name-band { position: absolute; left: 0; top: 179px; height: 61px; width: 540px; background: var(--white); }
  .eyebrow { position: absolute; left: 41px; top: 26px; font: 600 30px/1 'Poppins', sans-serif;
    letter-spacing: 10px; color: var(--white); }
  .headline { position: absolute; left: 39px; top: 62px; font: 800 68px/1 'Poppins', sans-serif;
    letter-spacing: -1.5px; color: var(--white); white-space: nowrap; }
  .streak { position: absolute; left: 41px; top: 136px; font: 500 40px/1 'Oswald', sans-serif;
    color: var(--navy); transform: scaleX(.82); transform-origin: left; letter-spacing: -.5px; white-space: nowrap; }
  .agent-name { position: absolute; left: 39px; top: 186px; font: 800 47px/1 'Poppins', sans-serif;
    letter-spacing: -1.5px; color: var(--navy); white-space: nowrap; }
  .contact-row { position: absolute; left: 41px; top: 246px; display: flex; align-items: center; gap: 10px; color: var(--white); }
  .phone-icon { width: 22px; height: 44px; }
  .agent-phone { font: 500 56px/1 'Oswald', sans-serif; transform: scaleX(.8); transform-origin: left;
    margin-right: -52px; letter-spacing: -1px; white-space: nowrap; }
  .divider { width: 2px; height: 40px; background: var(--white); margin: 0 8px; }
  .fee { font-family: 'Poppins', sans-serif; line-height: 1; white-space: nowrap; }
  .fee-rate { font-weight: 700; font-size: 24px; }
  .fee-label { font-weight: 500; font-size: 19px; letter-spacing: 1px; }
  .brand { position: absolute; left: 790px; top: 108px; width: 292px; display: flex;
    align-items: center; justify-content: center; gap: 10px; }
  .brand-dot { width: 16px; height: 16px; border-radius: 50%; background: var(--navy); flex: none; }
  .brand-name { font: 700 26px/1 'Poppins', sans-serif; color: var(--navy); white-space: nowrap; }
  .office-phone { position: absolute; left: 840px; top: 248px; width: 190px; height: 25px;
    border-radius: 13px; background: var(--navy); color: var(--white);
    font: 700 20px/25px 'Poppins', sans-serif; text-align: center; letter-spacing: 1px; }
  .office-address { position: absolute; left: 790px; top: 279px; width: 292px;
    display: flex; justify-content: center; }
  .office-address span { font: 500 22px/1 'Oswald', sans-serif; color: var(--navy);
    white-space: nowrap; transform: scaleX(.78); letter-spacing: -.2px; }
</style>
</head>
<body>
  <main class="billboard">
    <svg class="billboard-bg" width="1100" height="320" viewBox="0 0 1100 320" aria-hidden="true">
      <polygon points="0,0 731,0 559,320 0,320" fill="#a3a3a3"/>
      <polygon points="0,0 711,0 539,320 0,320" fill="#172f57"/>
    </svg>

    <div class="agent-photo" role="img" aria-label="Portrait of the realtor in a navy suit"></div>
    <div class="award-badge" role="img" aria-label="Local award badge"></div>

    <div class="accent-band"></div>
    <div class="name-band"></div>

    <p class="eyebrow">CORWYN'S</p>
    <h1 class="headline">BEST REALTOR</h1>
    <p class="streak">4 YEARS IN A ROW!</p>
    <h2 class="agent-name">TOBIAS WRENFIELD</h2>

    <div class="contact-row">
      <svg class="phone-icon" viewBox="0 0 22 44" aria-hidden="true">
        <rect x="1.5" y="1.5" width="19" height="41" rx="3" fill="none" stroke="#fff" stroke-width="3"/>
        <rect x="4" y="6" width="14" height="28" fill="#fff"/>
        <circle cx="11" cy="38.5" r="2" fill="#fff"/>
      </svg>
      <span class="agent-phone">555-214-7390</span>
      <span class="divider"></span>
      <div class="fee">
        <div class="fee-rate">1.75%</div>
        <div class="fee-label">LISTING FEE</div>
      </div>
    </div>

    <div class="brand">
      <span class="brand-dot"></span>
      <span class="brand-name">THE SUMMIT TEAM</span>
    </div>
    <p class="office-phone">855-555-0142</p>
    <p class="office-address"><span>2748 W AMBERLOW RD, BEL AIR, MD 20957</span></p>
  </main>
</body>
</html>
```